Valbrina Soletti Winery 2023 Label

We are just about to bottle our very first Napa Valley Cabernet Sauvignon and need label ideas

Target Market(s)

Cab drinkers who like Napa California Cabs

Industry/Entity Type

Wine Making

Logo Text

Valbrina Soletti 2023 Napa Estate Grown Cabernet Sauvignon

Requirements
Must have
• Winery Name, year of vintage and Napa Estate Cab
Nice to have
• If using the initials V and S use gold letters on black or red background

```html
<!DOCTYPE html>
<html lang="en">
<head>
<meta charset="utf-8">
<title>Valbrina Soletti – 2023 Napa Estate Grown Cabernet Sauvignon</title>
<link rel="stylesheet" href="https://fonts.googleapis.com/css2?family=Yellowtail&family=Playfair+Display:wght@600&display=swap">
<style>
  :root {
    --cream: #f7f1e1;
    --gold: #b58a26;
    --gold-light: #d4b25a;
    --berry: #a8294f;
    --white: #ffffff;
  }
  html, body {
    margin: 0;
    padding: 0;
    overflow: hidden;
  }
  .label {
    position: relative;
    width: 1200px;
    height: 1200px;
    background: var(--cream);
    overflow: hidden;
  }
  .winery-name {
    position: absolute;
    left: 0;
    width: 1200px;
    text-align: center;
    margin: 0;
    font-family: "Yellowtail", cursive;
    font-weight: 400;
    color: var(--gold);
    font-size: 150px;
    line-height: 1;
  }
  .winery-name.first { top: 108px; }
  .winery-name.second { top: 252px; }
  .crest {
    position: absolute;
    left: 380px;
    top: 395px;
    width: 440px;
    height: 420px;
  }
  .crest-year {
    font-family: "Playfair Display", serif;
    font-weight: 600;
    font-size: 36px;
    fill: var(--white);
  }
  .varietal {
    position: absolute;
    left: 0;
    width: 1200px;
    text-align: center;
    margin: 0;
    font-family: "Playfair Display", serif;
    font-weight: 600;
    color: var(--gold);
    line-height: 1;
  }
  .varietal.estate { top: 848px; font-size: 57px; }
  .varietal.cabernet { top: 922px; font-size: 57px; }
  .varietal.sauvignon { top: 980px; font-size: 100px; }
</style>
</head>
<body>
<main class="label">
  <h1 class="winery-name first">Valbrina</h1>
  <p class="winery-name second">Soletti</p>

  <svg class="crest" viewBox="0 0 440 420" xmlns="http://www.w3.org/2000/svg">
    <defs>
      <linearGradient id="crestFill" x1="0" y1="0" x2="0" y2="1">
        <stop offset="0" stop-color="#d9b965"/>
        <stop offset="0.45" stop-color="#efe3c2"/>
        <stop offset="1" stop-color="#e9d7a8"/>
      </linearGradient>
      <clipPath id="shieldClip">
        <path d="M 64 40 H 376 V 200 C 376 300 300 360 220 410 C 140 360 64 300 64 200 Z"/>
      </clipPath>
    </defs>
    <g role="img" aria-label="Crest illustration: grapevines with gold leaves and red grape clusters framing two glass bottles">
      <path d="M 64 40 H 376 V 200 C 376 300 300 360 220 410 C 140 360 64 300 64 200 Z" fill="url(#crestFill)"/>
    </g>
    <g clip-path="url(#shieldClip)">
      <rect x="0" y="336" width="440" height="90" fill="var(--gold)"/>
    </g>
    <path d="M 64 40 H 376 V 200 C 376 300 300 360 220 410 C 140 360 64 300 64 200 Z" fill="none" stroke="var(--gold)" stroke-width="6"/>
    <path d="M 76 52 H 364 V 200 C 364 292 294 348 220 396 C 146 348 76 292 76 200 Z" fill="none" stroke="var(--gold)" stroke-width="2"/>
    <text class="crest-year" x="220" y="376" text-anchor="middle">2023</text>
  </svg>

  <p class="varietal estate">NAPA ESTATE GROWN</p>
  <p class="varietal cabernet">CABERNET</p>
  <p class="varietal sauvignon">SAUVIGNON</p>
</main>
</body>
</html>
```